ebook cover for The Heron & The Badger (Squawk!)

We would like an ebook cover for a post Ph.D. on Animal Totems book called The Heron and The Badger. It is about human relationships and dating. Author is Marla Quenby Ph.D.
I am thinking perhaps just typographic with a fancy custom italicized or handwriting kind of font that fills the whole page, or a picture that doesn't belittle the fairytale of love. Something cosmic.
The subtitle to guide people, small, is "on dating"

```html
<!DOCTYPE html>
<html lang="en">
<head>
<meta charset="utf-8">
<title>The Heron and The Badger — On Dating</title>
<link rel="stylesheet" href="https://fonts.googleapis.com/css2?family=Kaushan+Script&family=Dancing+Script:wght@500&family=Libre+Baskerville&display=swap">
<style>
  :root {
    --page-bg: #f4f4f4;
    --sky-top: #88bde0;
    --sky-mid: #7fb2d8;
    --night-blue: #5f8fc0;
    --ground-black: #070707;
    --title-orange: #e8651f;
    --title-white: #ffffff;
    --title-black: #101010;
    --author-white: #f5f5f5;
  }
  * { margin: 0; padding: 0; box-sizing: border-box; }
  html, body {
    width: 1200px;
    height: 800px;
    overflow: hidden;
    background: var(--page-bg);
  }
  .cover {
    position: absolute;
    left: 373px;
    top: 30px;
    width: 454px;
    height: 740px;
    overflow: hidden;
    background: linear-gradient(180deg, var(--sky-top) 0%, var(--sky-mid) 50%);
    box-shadow: 0 6px 18px rgba(0,0,0,0.18);
  }
  .cover-scene {
    position: absolute;
    left: 0;
    top: 400px;
    width: 100%;
    height: 250px;
    background: linear-gradient(180deg,
      rgba(127,178,216,0) 0%,
      var(--night-blue) 30%,
      #4d79a8 65%,
      var(--ground-black) 100%);
  }
  .cover-ground {
    position: absolute;
    left: 0;
    top: 640px;
    width: 100%;
    height: 100px;
    background: var(--ground-black);
  }
  .title {
    position: absolute;
    inset: 0;
    z-index: 2;
    font-family: "Kaushan Script", cursive;
    line-height: 1;
  }
  .title span { position: absolute; white-space: nowrap; }
  .title-the-1 { left: 205px; top: 45px; font-size: 58px; color: var(--title-white); }
  .title-heron { left: 78px; top: 95px; font-size: 100px; color: var(--title-orange); }
  .title-and { left: 188px; top: 182px; font-size: 48px; color: var(--title-black); }
  .title-the-2 { left: 190px; top: 242px; font-size: 58px; color: var(--title-white); }
  .title-badger { left: 38px; top: 295px; font-size: 100px; color: var(--title-orange); }
  .subtitle {
    position: absolute;
    z-index: 2;
    left: 0;
    width: 100%;
    top: 585px;
    text-align: center;
    font-family: "Dancing Script", cursive;
    font-weight: 500;
    font-size: 44px;
    color: var(--title-orange);
  }
  .author {
    position: absolute;
    z-index: 2;
    left: 0;
    width: 100%;
    top: 690px;
    text-align: center;
    font-family: "Libre Baskerville", serif;
    font-size: 21px;
    letter-spacing: 6px;
    color: var(--author-white);
  }
</style>
</head>
<body>
  <main class="cover">
    <div class="cover-scene" role="img" aria-label="Moonlit night scene: full moon, silhouetted trees, a couple embracing holding heart balloons, butterflies and a bicycle in the grass"></div>
    <div class="cover-ground"></div>
    <h1 class="title" aria-label="The Heron and The Badger">
      <span class="title-the-1">The</span>
      <span class="title-heron">Heron</span>
      <span class="title-and">and</span>
      <span class="title-the-2">The</span>
      <span class="title-badger">Badger</span>
    </h1>
    <p class="subtitle">On Dating</p>
    <p class="author">Marla Quenby Ph.D.</p>
  </main>
</body>
</html>
```